Need corporate powerpoint template design for our sales proposals

Need corporate power point design template for our sales proposals. This powerpoint will be targeted at our customers when we are putting design proposals and pricing quotes together for them

Target Market(s)

Our customers

Industry/Entity Type

Sales

Requirements
Must have
• Brookvane name and logo somewhere
• Would like to have a cover slide and then non-cover slide as well as an ending slide for powerpoint templates
• Must have our corporate address and contact info somewhere, they are: Brookvane, Inc PO Box 47193 Oakland, California 94620. Office # 510-384-7159, email is info@brookvane-example.com
• I also attached an example business card to give you a sense of our design, also our website is www.brookvane-example.com
• Would like to match existing color scheme

```html
<!DOCTYPE html>
<html lang="en">
<head>
<meta charset="utf-8">
<title>About Us – Brookvane</title>
<link href="https://fonts.googleapis.com/css2?family=Lato:wght@400;700&display=swap" rel="stylesheet">
<style>
  :root {
    --brand-green: #68a82a;
    --page-bg: #f9f9f9;
    --body-grey: #6e6e6e;
    --white: #ffffff;
  }
  * { margin: 0; padding: 0; box-sizing: border-box; }
  html, body {
    width: 1200px;
    height: 685px;
    overflow: hidden;
    background: var(--page-bg);
  }
  .slide {
    position: relative;
    width: 1200px;
    height: 685px;
    background: var(--page-bg);
    font-family: "Lato", sans-serif;
    overflow: hidden;
  }
  .top-band {
    position: absolute;
    left: 0; top: 0;
    width: 1200px;
    height: 11px;
    background: var(--brand-green);
  }
  .brand-tab {
    position: absolute;
    right: 0; top: 0;
    width: 172px;
    height: 58px;
  }
  .brand-tab svg { position: absolute; inset: 0; }
  .brand-name {
    position: absolute;
    right: 16px;
    top: 18px;
    font-size: 25px;
    font-weight: 400;
    color: var(--white);
    letter-spacing: 0.2px;
  }
  .slide-title {
    position: absolute;
    left: 20px;
    top: 34px;
    font-size: 36px;
    font-weight: 700;
    color: var(--brand-green);
  }
  .section {
    position: absolute;
    left: 34px;
    width: 1120px;
  }
  .section-marker {
    position: absolute;
    left: 2px;
    top: 1px;
    width: 42px;
    height: 42px;
    border-radius: 50%;
    background: var(--brand-green);
  }
  .section-heading {
    margin-left: 69px;
    font-size: 32px;
    font-weight: 700;
    color: var(--brand-green);
    line-height: 40px;
  }
  .section-body {
    margin-left: 69px;
    margin-top: 1px;
    font-size: 21.3px;
    line-height: 32px;
    color: var(--body-grey);
  }
  .section--one { top: 137px; }
  .section--two { top: 305px; }
  .section--three { top: 486px; }
  .page-number {
    position: absolute;
    left: 1118px;
    top: 647px;
    width: 49px;
    height: 38px;
    background: var(--brand-green);
    color: var(--white);
    font-size: 15px;
    font-weight: 700;
    display: flex;
    align-items: center;
    justify-content: center;
  }
</style>
</head>
<body>
<div class="slide">
  <div class="top-band"></div>

  <div class="brand-tab">
    <svg width="172" height="58" viewBox="0 0 172 58">
      <polygon points="0,0 172,0 172,58 48,58" fill="var(--brand-green)"/>
    </svg>
    <span class="brand-name">Brookvane</span>
  </div>

  <h1 class="slide-title">About US</h1>

  <section class="section section--one">
    <span class="section-marker"></span>
    <h2 class="section-heading">SUBTITLE HERE</h2>
    <p class="section-body">Liquorice lolly loops applicake apple pie cupcake brownie bear claw&nbsp; cake gingerbread cotton candy. Bear claw croissant apple pie. Croissant cake sweet puff wafer . Liquorice lolly loops applicake apple pie cupcake brownie bear claw&nbsp; cake gingerbread cotton candy.</p>
  </section>

  <section class="section section--two">
    <span class="section-marker"></span>
    <h2 class="section-heading">SUBTITLE HERE</h2>
    <p class="section-body">Liquorice lolly loops applicake apple pie cupcake brownie bear claw&nbsp; cake gingerbread cotton candy. Bear claw croissant apple pie. Croissant cake sweet puff wafer . Liquorice lolly loops applicake apple pie cupcake brownie bear claw&nbsp; cake gingerbread cotton candy.</p>
  </section>

  <section class="section section--three">
    <span class="section-marker"></span>
    <h2 class="section-heading">SUBTITLE HERE</h2>
    <p class="section-body">Liquorice lolly loops applicake apple pie cupcake brownie bear claw&nbsp; cake gingerbread cotton candy. Bear claw croissant apple pie. Croissant cake sweet puff wafer . Liquorice lolly loops applicake apple pie cupcake brownie bear claw&nbsp; cake gingerbread cotton candy.</p>
  </section>

  <div class="page-number">01</div>
</div>
</body>
</html>
```